Werbeplakat für neues Webradio
Die Designerin konnte sich optimal in meine Wünsche und Vorstellungen hinein denken. ich bin mit dem Endresultat mehr als zufrieden.
Zielgruppe
Wir starten gerade ein kleines Webradio für eine sehr ländliche Region mit vielen Hügeln und viel Landwirtschaft. Daher auch der Name: Wiesenfunker.de Das Talwelle - Radio.
Wir sind nicht zu jung, aber auch nicht zu alt. Wir sind "Landeier" und stolz darauf.
Wir liefern neue Musik und Neues von hier. Wir sind nah am Leben und nah an den Menschen. Wir sind eigen - wir sind wir.Wir sind mittendrin - wir sind echte Wiesenfunker :-)
Aufgabenstellung
Liebe Designer.
Begleitend zum Sendestart unseres Webradios wollen wir mit einer Flyer- und Plakat-Kampagne auf uns aufmerksam machen.
Es soll ein absoluter Eyecatcher werden und für den nötigen "Talk of Dorf" sorgen.
Nicht zu spießig, aber auch nicht zu jung.
Jeder soll nach dem Betrachten Lust haben einfach mal reinzuhören!!!
Verwendet werden sollen unser Logo und der beinhaltete Name
"Wiesenfunker.de - Das Talwelle Radio".
Wo und wie Ihr alles platziert, wisst ihr besser als ich!
Zudem bitte folgende Textelemente: (Anordnung wie ihr es am besten findet)
-Neue Musik und Neues von hier
-Jetzt einschalten - Im Web oder per App - www.wiesenfunker.de
Irgendwo auf dem Plakat sollte noch etwas Platz bleiben, auf dem später hoffentlich die Logos von Sponsoren bzw. Werbekunden auftauchen werden. :-)
Unser Logo habe ich beigefügt (in mehreren Dateiformen)
Ich bin sehr gespannt auf Eure Umsetzungen und danke jedem der mitmacht von Herzen für seinen/ihren Einsatz!
Wenn Fragen da sind - einfach her damit. Ich antworte zeitnah
Cheerio
Rüdiger

```html
<!DOCTYPE html>
<html lang="de">
<head>
<meta charset="utf-8">
<title>Wiesenfunker.de – Das Talwelle-Radio – Plakat</title>
<link rel="stylesheet" href="https://fonts.googleapis.com/css2?family=Saira+Extra+Condensed:wght@500;600&family=Open+Sans:wght@400;700&display=swap">
<style>
  :root {
    --sky-top: #8fc3d6;
    --sky-mid: #6f7f88;
    --cloud: #a9b2b3;
    --wheat: #c99a45;
    --wheat-deep: #8a5f22;
    --orange: #e2640e;
    --white: #ffffff;
    --grey: #7d7d7d;
  }
  * { margin: 0; padding: 0; box-sizing: border-box; }
  html, body { width: 849px; height: 1200px; overflow: hidden; background: var(--white); }
  .poster {
    position: relative;
    width: 849px;
    height: 1200px;
    overflow: hidden;
    background: var(--white);
  }
  .hero-photo {
    position: absolute;
    inset: 0 0 200px 0;
    background: linear-gradient(180deg,
      var(--sky-top) 0%,
      var(--cloud) 22%,
      var(--sky-mid) 40%,
      #5c6a6e 46%,
      var(--wheat) 50%,
      #d6aa57 70%,
      var(--wheat-deep) 100%);
  }
  .artwork {
    position: absolute;
    left: 0; top: 0;
    width: 849px; height: 1200px;
  }
  .artwork text {
    font-family: "Saira Extra Condensed", "Arial Narrow", sans-serif;
  }
  .headline-line { fill: var(--white); font-weight: 500; font-size: 122px; }
  .cta-line { fill: var(--white); font-weight: 600; font-size: 40px; }
  .brand-name { fill: var(--orange); font-weight: 600; font-size: 46px; }

  .sponsor-row {
    position: absolute;
    left: 0; top: 1154px;
    width: 849px;
    height: 30px;
    font-family: "Open Sans", Arial, sans-serif;
    font-size: 15px;
    color: var(--grey);
  }
  .sponsor {
    position: absolute;
    top: 0;
    display: flex;
    align-items: center;
    gap: 6px;
    height: 28px;
    white-space: nowrap;
  }
  .sponsor .mark { width: 19px; height: 19px; background: var(--grey); flex: none; }
  .sponsor .mark.round { width: 26px; height: 26px; border-radius: 50%; }
  .sponsor .mark.frame { width: 26px; height: 26px; background: none; border: 3px solid var(--grey); }
  .sponsor.bold { font-weight: 700; }
  .sponsor-1 { left: 133px; }
  .sponsor-2 { left: 285px; }
  .sponsor-3 { left: 441px; }
  .sponsor-4 { left: 591px; }
</style>
</head>
<body>
<main class="poster">
  <div class="hero-photo" role="img" aria-label="Fröhliche Frau springt mit einem wehenden orangefarbenen Tuch über den Kopf durch ein goldenes Kornfeld unter bewölktem Himmel"></div>

  <svg class="artwork" viewBox="0 0 849 1200">
    <defs>
      <filter id="headline-shadow" x="-5%" y="-20%" width="115%" height="150%">
        <feDropShadow dx="2" dy="3" stdDeviation="2" flood-color="#000" flood-opacity="0.45"/>
      </filter>
    </defs>

    <path class="white-swoosh" d="M0,1095 Q480,935 849,960 L849,1200 L0,1200 Z" fill="var(--white)"/>

    <g class="headline" filter="url(#headline-shadow)">
      <text class="headline-line" x="238" y="667" textLength="413" lengthAdjust="spacingAndGlyphs">Neue Musik</text>
      <text class="headline-line" x="437" y="750" textLength="371" lengthAdjust="spacingAndGlyphs">und Neues</text>
      <text class="headline-line" x="437" y="844" textLength="287" lengthAdjust="spacingAndGlyphs">von hier</text>
    </g>

    <circle class="brand-mark" cx="378" cy="1062" r="48" fill="var(--orange)"/>

    <g class="cta-band" transform="translate(0 1090) rotate(-11.2)">
      <rect x="-30" y="-95" width="659" height="95" rx="12" fill="var(--orange)"/>
      <text class="cta-line" x="28" y="-58" textLength="580" lengthAdjust="spacingAndGlyphs">Jetzt einschalten – Im Web oder per App</text>
      <text class="cta-line" x="25" y="-17" textLength="290" lengthAdjust="spacingAndGlyphs">www.wiesenfunker.de</text>
    </g>

    <g class="brand">
      <text class="brand-name" x="472" y="1059">Wiesenfunker.de</text>
      <text class="brand-name" x="472" y="1098" textLength="323" lengthAdjust="spacingAndGlyphs">Das Talwelle-Radio</text>
    </g>
  </svg>

  <footer class="sponsor-row">
    <div class="sponsor sponsor-1"><span class="mark"></span>Muster Logo</div>
    <div class="sponsor sponsor-2 bold"><span class="mark frame"></span>Muster Logo</div>
    <div class="sponsor sponsor-3"><span class="mark round"></span>Muster Logo</div>
    <div class="sponsor sponsor-4"><span class="mark"></span>Muster Logo</div>
  </footer>
</main>
</body>
</html>
```